KLWB Canberra Pty Ltd

Want something creative and that catches your eye. We are a traffic control companythat offers all aspects of traffic control from planning to roadworks.

Contact Information for Business Card

Dean Morrow - Director
Ph: 0419 583 216
Email: dean@klwb.com.au
27 Vane Harbin ct Larwood ACT 2908

```html
<!DOCTYPE html>
<html lang="en">
<head>
<meta charset="utf-8">
<title>KLWB Canberra – Business Card</title>
<link rel="stylesheet" href="https://fonts.googleapis.com/css2?family=Michroma&display=swap">
<style>
  :root {
    --stage: #3b3b3b;
    --stage-edge: #1f1f1f;
    --card: #1b1b1b;
    --card-soft: #262626;
    --gold-light: #e3cc3c;
    --gold-dark: #b8901f;
    --text-light: #d9d9d9;
    --text-gold: #b39c3c;
    --brand-mark: #8cc063;
  }
  * { box-sizing: border-box; margin: 0; padding: 0; }
  html, body {
    width: 1200px; height: 900px; overflow: hidden;
  }
  body {
    background: radial-gradient(ellipse at 50% 35%, var(--stage) 0%, var(--stage-edge) 100%);
    font-family: "Michroma", sans-serif;
    display: flex; align-items: center; justify-content: center; gap: 40px;
  }
  .card {
    position: relative;
    width: 520px; height: 316px;
    background: linear-gradient(120deg, var(--card) 45%, var(--card-soft) 100%);
    box-shadow: 0 14px 30px rgba(0,0,0,.55);
    overflow: hidden;
  }
  .card-accent {
    position: absolute; top: 0; right: 0;
    width: 110px; height: 100%;
    background: linear-gradient(160deg, var(--gold-dark) 0%, var(--gold-light) 100%);
    opacity: .85;
  }
  .brand {
    position: absolute; left: 40px; top: 140px;
    display: flex; align-items: center; gap: 12px;
  }
  .brand-mark { width: 34px; height: 34px; background: var(--brand-mark); }
  .brand-name { color: var(--text-light); font-size: 20px; letter-spacing: 1px; }
  .person { position: absolute; left: 40px; top: 100px; }
  .person-name { color: var(--text-light); font-size: 23px; font-weight: 400; letter-spacing: 2px; }
  .person-role { color: var(--text-gold); font-size: 19px; letter-spacing: 2px; margin-top: 8px; }
  .contact {
    position: absolute; left: 40px; top: 216px;
    color: var(--text-light); font-size: 11px; line-height: 18px;
    letter-spacing: 1px; text-transform: uppercase; list-style: none;
  }
</style>
</head>
<body>
  <section class="card card-front">
    <div class="card-accent" role="img" aria-label="Gold hazard stripe decoration"></div>
    <div class="brand">
      <span class="brand-mark"></span>
      <span class="brand-name">KLWB CANBERRA</span>
    </div>
  </section>

  <section class="card card-back">
    <div class="card-accent" role="img" aria-label="Gold hazard stripe decoration"></div>
    <div class="person">
      <h1 class="person-name">DEAN MORROW</h1>
      <p class="person-role">DIRECTOR</p>
    </div>
    <ul class="contact">
      <li>Ph: 0419 583 216</li>
      <li>Email: dean@klwb.com.au</li>
      <li>27 Vane Harbin ct Larwood ACT 2908</li>
    </ul>
  </section>
</body>
</html>
```